Catchy Cards for Hospital

I run a rural hospital in Texas called Pellor Valley Hospital and am in need of contemporary business cards for all of my Department Heads. While our logo is somewhat simplistic, I don't have the option of changing it at this time, so anything to make the rest of the card present the appearance of a modern, professional healthcare facility would be great. Although the attached files are in black, our hospital colors are in a copper brown and black. I need to be able to change the name and title on the card so I can get cards printed for various department heads.

Target Market(s)

Referring physicians, large hospital systems, national organizations, state and federal government

Industry/Entity Type

Hospital

Contact Information for Business Card

Name Dale Hoskin
Title CEO

Phone: Main 521-555-0147 & Direct xxxxxx
Fax xxxxx
dale.hoskin@pellorvh.example
382 Wimble Street Box 415
Hollis Ford, Wexland 76902

Font styles to use
Serif

Colors
f48340

Requirements
Must have
• Clean crisp lines and ability to modify names, titles and emails
• On the back "PellorValleyHospital.Example
Nice to have
• Needs to be in line with logo, which is a bit dated and not too appealing, but I'm hoping that the rest of the card can make up for that fact just a little bit.
• Hospital's colors are a copper brown, black and white
Should not have
• Shapes or anything distracting

```html
<!DOCTYPE html>
<html lang="en">
<head>
<meta charset="utf-8">
<title>Pellor Valley Hospital – Business Card</title>
<link href="https://fonts.googleapis.com/css2?family=Jost:wght@400;500;600&display=swap" rel="stylesheet">
<style>
  :root {
    --stage: #2b2b2b;
    --paper: #ffffff;
    --ink: #1c1c1c;
    --copper: #f48340;
    --rule: #222222;
    --band-edge: #111111;
  }
  * { margin: 0; padding: 0; box-sizing: border-box; }
  html, body {
    width: 1200px; height: 900px; overflow: hidden;
    background: var(--stage);
    font-family: "Jost", "Futura", sans-serif;
    color: var(--ink);
  }
  .stage {
    position: relative; width: 1200px; height: 900px;
    display: flex; flex-direction: column; align-items: center; justify-content: center;
    gap: 40px;
  }
  .card {
    position: relative; width: 630px; height: 360px;
    background: var(--paper); overflow: hidden;
  }

  .wordmark {
    font-weight: 600; color: var(--ink);
    font-size: 38px; line-height: 1.02; letter-spacing: 0.5px;
  }

  /* back side */
  .card-back .wordmark {
    position: absolute; left: 0; right: 0; top: 92px;
    text-align: center;
  }
  .card-back .site {
    position: absolute; left: 0; right: 0; bottom: 36px;
    text-align: center; font-size: 15px; letter-spacing: 1.2px; font-weight: 400;
  }

  /* front side */
  .card-front .wordmark {
    position: absolute; left: 48px; top: 96px; width: 250px;
    font-size: 40px;
  }
  .divider {
    position: absolute; left: 318px; top: 70px; width: 2px; height: 196px;
    background: var(--rule);
  }
  .details {
    position: absolute; left: 342px; top: 78px;
  }
  .person-name {
    font-size: 24px; font-weight: 600; color: var(--copper);
    letter-spacing: 2px; text-transform: uppercase; line-height: 1;
  }
  .person-title {
    font-size: 17px; font-weight: 400; letter-spacing: 1px; margin-top: 4px;
  }
  .address {
    font-size: 15px; line-height: 1.3; letter-spacing: 1.2px; margin-top: 18px;
  }
  .contacts { list-style: none; margin-top: 8px; }
  .contacts li {
    display: flex; align-items: center; gap: 12px;
    font-size: 15px; letter-spacing: 1.2px; line-height: 1.5;
  }
  .contacts svg { width: 12px; height: 12px; flex: none; fill: var(--copper); }
  .swoosh {
    position: absolute; left: 0; bottom: 0; width: 630px; height: 72px;
  }
</style>
</head>
<body>
<main class="stage">

  <section class="card card-back" aria-label="Card back">
    <div class="wordmark">Pellor<br>Valley<br>Hospital</div>
    <p class="site">PellorValleyHospital.Example</p>
  </section>

  <section class="card card-front" aria-label="Card front">
    <div class="wordmark">Pellor<br>Valley<br>Hospital</div>
    <div class="divider"></div>
    <div class="details">
      <h1 class="person-name">Dale Hoskin</h1>
      <p class="person-title">CEO</p>
      <p class="address">382 Wimble Street Box 415<br>Hollis Ford, Wexland 76902</p>
      <ul class="contacts">
        <li>
          <svg viewBox="0 0 12 12" aria-hidden="true"><path d="M2.4 0.6 4.3 2.8 3.3 4.3c.7 1.6 2 2.9 3.6 3.6l1.5-1 2.2 1.9-1.2 2C5 10.6 1.4 7 .6 1.8z"/></svg>
          <span>521-555-0147</span>
        </li>
        <li>
          <svg viewBox="0 0 12 12" aria-hidden="true"><path d="M3 0h6v12H3zM4.2 1.2v8.4h3.6V1.2z"/></svg>
          <span>000-123-4567</span>
        </li>
        <li>
          <svg viewBox="0 0 12 12" aria-hidden="true"><path d="M3 0h6v3H3zM0 4h12v5H9.5v3h-7V9H0zM3.5 8v3h5V8z"/></svg>
          <span>000-123-4567</span>
        </li>
        <li>
          <svg viewBox="0 0 12 12" aria-hidden="true"><path d="M0 2h12L6 6.5zM0 3.3l6 4.5 6-4.5V10H0z"/></svg>
          <span>dale.hoskin@pellorvh.example</span>
        </li>
      </ul>
    </div>
    <svg class="swoosh" viewBox="0 0 630 72" preserveAspectRatio="none" aria-hidden="true">
      <path d="M260 34 C400 42 530 52 630 62 L630 70 C520 58 400 46 260 34 Z" fill="var(--band-edge)"/>
      <path d="M0 4 C220 18 440 42 630 68 L630 72 L0 72 Z" fill="var(--copper)"/>
    </svg>
  </section>

</main>
</body>
</html>
```